Nora Pettifer Music EP Design Artwork

EP musical recording cover art work. Nora Pettifer is a new artist in the Pop, Country Pop, Pop Rock, Americana and Singer-songwriter genres. The name of the EP is "Where the River Bends", and her first single is being released on all streaming platforms globally June 1st. We are looking for a graphic design that has that Pop/rock female artist appeal. norapettifer.net and all social media outlets are norapettifersongs (reference). Your art work will be seen globally and we will give a personal shout out on all her socials to the design we select as a single post. Her signature logo is attached for a color and style example. Please try to use the signature within the EP cover design, but feel free to change the purple backing accordingly if another color is needed to fit better with the color scheme of your design.

Requirements
Must have
• Nora Pettifer signature logo and EP name

Some of you asked for hi res pics, use this link:

https://files.quillbox.net/share/u/0/folders/8kTzW3pLqR2vN7xYcD4mHs1JbE6uAfGoQ
Should not have
• June 1 on the EP art work. June 1 is the release of the first single on the EP. This is an album cover, we want it to look like a really cool pop female artist album cover, thanks.

```html
<!DOCTYPE html>
<html lang="en">
<head>
<meta charset="utf-8">
<title>Nora Pettifer – Where the River Bends EP Cover</title>
<link rel="stylesheet" href="https://fonts.googleapis.com/css2?family=Libre+Baskerville:wght@400;700&display=swap">
<style>
  :root {
    --page: #ffffff;
    --ochre-light: #e9b85e;
    --ochre-mid: #e1b076;
    --ochre-deep: #d7a46a;
    --hair: #b07a4a;
    --skin: #e6b597;
    --jacket: #15110f;
    --title: #ffffff;
    --title-red: #c21f3a;
    --title-violet: #5b2bc4;
    --name: #ffffff;
  }
  * { margin: 0; padding: 0; box-sizing: border-box; }
  html, body {
    width: 1200px;
    height: 720px;
    overflow: hidden;
    background: var(--page);
  }
  .canvas {
    position: relative;
    width: 1200px;
    height: 720px;
  }
  .ep-cover {
    position: absolute;
    left: 359px;
    top: 120px;
    width: 480px;
    height: 478px;
    overflow: hidden;
    background: linear-gradient(160deg, var(--ochre-light) 0%, var(--ochre-mid) 55%, var(--ochre-deep) 100%);
    box-shadow: 6px 6px 8px rgba(0, 0, 0, 0.18);
  }
  .portrait {
    position: absolute;
    left: 0;
    top: 20px;
    width: 286px;
    height: 458px;
    border-radius: 130px 130px 0 0;
    background: linear-gradient(180deg, var(--hair) 0%, var(--skin) 28%, var(--skin) 48%, #3a2a24 62%, var(--jacket) 76%, var(--jacket) 100%);
  }
  .ep-title {
    position: absolute;
    left: 266px;
    top: 124px;
    width: 197px;
    padding: 9px 0 8px;
    border-top: 2px solid var(--title);
    border-bottom: 2px solid var(--title);
    font-family: "Libre Baskerville", serif;
    font-weight: 400;
    font-size: 24px;
    line-height: 1.25;
    color: var(--title);
    text-transform: uppercase;
    white-space: nowrap;
    text-shadow: 1px 1px 0 var(--title-red), -1px 0 0 var(--title-violet);
  }
  .artist-name {
    position: absolute;
    left: 28px;
    top: 338px;
    font-family: "Libre Baskerville", serif;
    font-weight: 700;
    font-size: 54px;
    line-height: 1;
    color: var(--name);
    white-space: nowrap;
  }
</style>
</head>
<body>
  <main class="canvas">
    <section class="ep-cover">
      <div class="portrait" role="img" aria-label="Portrait photograph of the artist, long straight hair, black jacket over a snakeskin-print top"></div>
      <h1 class="ep-title">Where the<br>River Bends</h1>
      <p class="artist-name">Nora Pettifer</p>
    </section>
  </main>
</body>
</html>
```